SUMMIT GATHERING 2021. August 20th -22nd.

The Hosts of the conference: Grace Tabernacle-Pastors Ron n Della ( Picture with two persons)

Guest Minister: Bishop Lucinda Okotieno. (Cedar Ridge Awakening)

Venue:
Sealand Gateway Lodgeview. 4817 North 239th Avenue Seattle, WA 98174.

Conference times.
Friday August 20th 6pm-8:30pm
Saturday August 21st. 6pm-8:30pm

Sunday August 22nd 10am-1pm
“ CHURCH RENEWAL GATHERING”

5pm-7:30pm
TWOFOLD SURGE GATHERING.

Target Market(s)

18-55

Industry/Entity Type

Religious/ Entertainment.

Requirements
Must have
• A highlight of the Relaunch service on Sunday August 22nd 5pm-7:30pm.
Nice to have
• Excellent ideas….

```html
<!DOCTYPE html>
<html lang="en">
<head>
<meta charset="utf-8">
<title>Summit Gathering 2021 – Church Renewal Gathering</title>
<link rel="stylesheet" href="https://fonts.googleapis.com/css2?family=Montserrat:wght@800;900&family=Open+Sans:wght@300;400;600;700;800&family=Playfair+Display:ital,wght@1,500&display=swap">
<style>
  :root {
    --paper: #e9e9ea;
    --white: #ffffff;
    --brown-deep: #2b170c;
    --brown: #5a3217;
    --brown-mid: #6e4426;
    --tan: #c29c72;
    --taupe: #b2a08f;
    --ink: #2a1d14;
  }
  * { margin: 0; padding: 0; box-sizing: border-box; }
  html, body { width: 849px; height: 1200px; overflow: hidden; background: var(--paper); }
  .poster {
    position: relative; width: 849px; height: 1200px; overflow: hidden;
    background: linear-gradient(180deg, #ececed 0%, #f4f4f4 60%, #e6e6e7 100%);
    font-family: "Open Sans", sans-serif; color: var(--white);
  }
  .backdrop { position: absolute; inset: 0; }
  .abs { position: absolute; }

  .event-title { left: 0; width: 849px; top: 32px; text-align: center; }
  .event-title .name {
    display: inline-block; background: var(--white); color: var(--brown);
    font-weight: 800; font-size: 42px; line-height: 1; letter-spacing: -0.5px;
    padding: 6px 12px 4px; border-radius: 12px;
  }
  .event-title .year {
    display: inline-block; margin-top: 4px; background: var(--white); color: var(--brown);
    font-weight: 800; font-size: 74px; line-height: 0.95; letter-spacing: -1px;
    padding: 0 14px 4px; border-radius: 14px;
  }

  .brand-mark {
    left: 717px; top: 10px; width: 102px; height: 121px;
    background: var(--brown-deep); border: 2px solid #8f7358;
    display: flex; flex-direction: column; align-items: center; justify-content: center; gap: 10px;
  }
  .brand-mark .dot { width: 40px; height: 40px; border-radius: 50%; background: var(--tan); }
  .brand-mark .label {
    color: var(--tan); font-weight: 700; font-size: 10px; letter-spacing: 0.5px;
    text-align: center; line-height: 1.2;
  }

  .dates {
    left: 0; width: 849px; top: 216px; text-align: center;
    color: var(--tan); font-weight: 700; font-size: 33px; letter-spacing: -0.3px;
  }
  .dates sup { font-size: 19px; vertical-align: 14px; }

  .headline-main {
    left: 0; width: 849px; top: 306px; text-align: center;
    font-family: "Montserrat", sans-serif; font-weight: 900; font-size: 136px;
    line-height: 1; letter-spacing: -3px; color: var(--white);
  }
  .headline-sub {
    left: 0; width: 849px; top: 446px; text-align: center;
    font-weight: 700; font-size: 92px; line-height: 1; letter-spacing: -2px; color: var(--tan);
  }
  .headline-script {
    right: 118px; top: 500px;
    font-family: "Playfair Display", serif; font-style: italic; font-weight: 500;
    font-size: 78px; line-height: 1; color: var(--white);
  }

  .info-head { color: var(--tan); font-weight: 700; font-size: 25px; line-height: 1; letter-spacing: -0.4px; }
  .info-line { font-weight: 400; font-size: 19px; line-height: 25px; color: var(--white); }

  .schedule { right: 449px; top: 628px; text-align: right; }
  .schedule .slot { margin-top: 10px; }
  .schedule .slot + .slot { margin-top: 21px; }

  .divider { left: 423px; top: 624px; width: 2px; height: 228px; background: var(--white); }

  .venue { left: 446px; top: 628px; }
  .venue .address { margin-top: 10px; }
  .venue .highlight { margin-top: 12px; line-height: 26px; }
  .venue .highlight-time { margin-top: 2px; }

  .portrait {
    width: 190px; height: 190px; border-radius: 50%; border: 3px solid var(--white);
    box-shadow: 0 0 0 1px rgba(0,0,0,0.08);
  }
  .portrait.hosts { left: 84px; top: 905px; background: radial-gradient(circle at 45% 40%, #7a4a3c 0%, #40202a 55%, #6a2f6e 100%); }
  .portrait.guest { left: 582px; top: 904px; background: radial-gradient(circle at 50% 40%, #5a3a2c 0%, #3d2a22 45%, #c7d5c6 100%); }

  .caption { color: var(--ink); text-align: center; font-weight: 700; }
  .caption .role { font-size: 15px; line-height: 21px; }
  .caption .who { font-size: 19px; line-height: 25px; }
  .caption.hosts { left: 18px; width: 320px; top: 1108px; }
  .caption.hosts .who { margin-top: 2px; white-space: nowrap; }
  .caption.guest { left: 505px; width: 300px; top: 1100px; }
  .caption.guest .who:first-of-type { margin-top: 4px; }
</style>
</head>
<body>
<main class="poster">
  <svg class="backdrop" width="849" height="1200" viewBox="0 0 849 1200" role="img" aria-label="Photo of a church interior with stained glass windows, toned in deep brown">
    <defs>
      <linearGradient id="sanctuaryTone" x1="0" y1="0" x2="0.6" y2="1">
        <stop offset="0" stop-color="#3a2010"/>
        <stop offset="0.45" stop-color="#5b3519"/>
        <stop offset="0.75" stop-color="#4a2a14"/>
        <stop offset="1" stop-color="#2e1a0d"/>
      </linearGradient>
    </defs>
    <polygon points="560,0 849,0 849,290" fill="var(--taupe)"/>
    <polygon points="0,70 170,0 520,0 849,330 849,1000 560,900 300,900 0,760" fill="url(#sanctuaryTone)"/>
  </svg>

  <header class="abs event-title">
    <div class="name">SUMMIT GATHERING</div><br>
    <div class="year">2021</div>
  </header>

  <div class="abs brand-mark">
    <span class="dot"></span>
    <span class="label">GRACE<br>TABERNACLE</span>
  </div>

  <p class="abs dates">AUGUST 20<sup>TH</sup> -22<sup>ND</sup></p>

  <h1 class="abs headline-main">CHURCH</h1>
  <p class="abs headline-sub">RENEWAL</p>
  <p class="abs headline-script">Gathering</p>

  <section class="abs schedule">
    <h2 class="info-head">CONFERENCE TIMES</h2>
    <div class="slot"><p class="info-line">Friday August 20th</p><p class="info-line">6pm-8:30pm</p></div>
    <div class="slot"><p class="info-line">Saturday August 21st</p><p class="info-line">6pm-8:30pm</p></div>
    <div class="slot"><p class="info-line">Sunday August 22nd</p><p class="info-line">10am-1pm</p></div>
  </section>

  <div class="abs divider"></div>

  <section class="abs venue">
    <h2 class="info-head">VENUE</h2>
    <p class="info-line address">Sealand Gateway Lodgeview. 4817<br>North 239th Avenue Seattle,<br>WA 98174.</p>
    <h2 class="info-head highlight">TWOFOLD<br>SURGE GATHERING.</h2>
    <p class="info-line highlight-time">Sunday August 22nd<br>5pm-7:30pm</p>
  </section>

  <div class="abs portrait hosts" role="img" aria-label="Photo of the hosts, Pastors Ron and Della"></div>
  <div class="abs portrait guest" role="img" aria-label="Photo of the guest minister, Bishop Lucinda Okotieno"></div>

  <div class="abs caption hosts">
    <p class="role">The Hosts<br>of the conference:</p>
    <p class="who">Grace Tabernacle-Pastors Ron n Della</p>
  </div>
  <div class="abs caption guest">
    <p class="role">Guest Minister</p>
    <p class="who">Bishop Lucinda Okotieno</p>
    <p class="who">(Cedar Ridge Awakening)</p>
  </div>
</main>
</body>
</html>
```